"Thornbury Accupuncture" needs a Promotional Card - A6 size

Requirements
Must have
• Bright colours, pictures of happy people, acupuncture-related pictures.

```html
<!DOCTYPE html>
<html lang="en">
<head>
<meta charset="utf-8">
<title>Thornbury Acupuncture – Promotional Card</title>
<link rel="stylesheet" href="https://fonts.googleapis.com/css2?family=Raleway:wght@400;500;700;800;900&display=swap">
<style>
  :root {
    --stage: #ececec;
    --brand-red: #e8432a;
    --paper-white: #fffdf8;
    --cream: #fff3cf;
    --sun: #fed35f;
    --peach: #f6a25a;
    --orange: #f08a3c;
    --sky: #fbf6ee;
    --plum: #7b5a78;
  }
  * { margin: 0; padding: 0; box-sizing: border-box; }
  html, body {
    width: 1200px; height: 1000px; overflow: hidden;
    background: var(--stage);
    font-family: "Raleway", Arial, sans-serif;
  }
  .promo-card {
    position: absolute; left: 289px; top: 82px;
    width: 622px; height: 876px; overflow: hidden;
    background: linear-gradient(180deg, var(--paper-white) 0%, var(--paper-white) 45%, var(--cream) 62%, var(--sun) 100%);
    box-shadow: 0 2px 8px rgba(0,0,0,0.18);
  }
  .hero { position: absolute; left: 0; top: 0; width: 622px; height: 420px; }
  .brand {
    position: absolute; left: 400px; top: 372px; width: 210px;
    text-align: center; color: var(--brand-red);
    font-weight: 800; font-size: 22px; line-height: 22px;
  }
  .brand-dot {
    display: block; width: 18px; height: 18px; margin: 0 auto 8px;
    border-radius: 50%; background: var(--brand-red);
  }
  .headline { position: absolute; left: 0; top: 462px; width: 622px; text-align: center; color: var(--brand-red); }
  .headline-lead { font-size: 44px; font-weight: 400; letter-spacing: 1px; line-height: 50px; }
  .headline-main { font-size: 61px; font-weight: 800; line-height: 62px; letter-spacing: 0.5px; }
  .headline-rule { position: absolute; left: 46px; top: 573px; width: 530px; height: 3px; background: var(--brand-red); }
  .body-copy {
    position: absolute; left: 48px; top: 592px; width: 528px;
    color: var(--brand-red); font-size: 9.6px; line-height: 12.4px; text-align: justify;
  }
  .body-copy p + p { margin-top: 6px; }
  .offer-band {
    position: absolute; left: 0; top: 704px; width: 622px; height: 46px;
    background: var(--brand-red); color: #fff; text-align: center;
    font-size: 21px; font-weight: 500; line-height: 46px; letter-spacing: 0.3px;
  }
  .price { position: absolute; top: 755px; height: 56px; line-height: 56px; text-align: center; font-size: 32px; font-weight: 400; }
  .price-weekday { left: 0; width: 312px; background: var(--brand-red); color: #fff; }
  .price-weekend { left: 313px; width: 309px; background: #fff; color: var(--brand-red); }
  .price-amount { font-weight: 900; font-size: 36px; }
  .price-amount sup { font-size: 20px; vertical-align: 14px; margin-left: 6px; }
  .contact {
    position: absolute; top: 837px; font-size: 14.5px; color: var(--brand-red);
  }
  .contact-web { left: 32px; }
  .contact-tel { right: 28px; }
</style>
</head>
<body>
  <main class="promo-card">
    <svg class="hero" viewBox="0 0 622 420" xmlns="http://www.w3.org/2000/svg">
      <defs>
        <linearGradient id="treatmentTone" x1="0" y1="0" x2="0" y2="1">
          <stop offset="0" stop-color="#fbf4ea"/>
          <stop offset="0.5" stop-color="#f7c9a0"/>
          <stop offset="1" stop-color="#d9895a"/>
        </linearGradient>
        <linearGradient id="familyTone" x1="0" y1="0" x2="1" y2="1">
          <stop offset="0" stop-color="#f9d9a8"/>
          <stop offset="1" stop-color="#f3a35c"/>
        </linearGradient>
        <linearGradient id="portraitTone" x1="0" y1="0" x2="0" y2="1">
          <stop offset="0" stop-color="#fde7b4"/>
          <stop offset="0.55" stop-color="#f6b56c"/>
          <stop offset="1" stop-color="#8a5b6f"/>
        </linearGradient>
      </defs>
      <rect width="622" height="420" fill="url(#treatmentTone)" role="img" aria-label="Photo of a woman receiving acupuncture needles on her forehead"/>
      <path d="M300 0 L410 0 L410 180 Q300 160 230 230 L0 260 L0 180 Z" fill="url(#familyTone)" opacity="0.75" role="img" aria-label="Photo of a smiling grandfather with two grandchildren"/>
      <path d="M0 300 Q120 200 300 230 L330 420 L0 420 Z" fill="#e69a5c" opacity="0.8" role="img" aria-label="Photo of a happy older couple embracing"/>
      <path d="M380 0 L622 0 L622 330 L375 330 Z" fill="url(#portraitTone)" role="img" aria-label="Portrait photo of the acupuncturist"/>
      <path d="M0 388 Q110 370 222 413 Q380 300 622 318 L622 420 L0 420 Z" fill="var(--paper-white)"/>
    </svg>

    <div class="brand"><span class="brand-dot"></span>thornbury<br>acupuncture</div>

    <h1 class="headline">
      <span class="headline-lead">ALWAYS WANT TO TRY</span><br>
      <span class="headline-main">ACUPUNCTURE?</span>
    </h1>
    <div class="headline-rule"></div>

    <div class="body-copy">
      <p>The way you begin your day sets the tone for the rest of the day. Over time, it sets the tone for your long-term health. Here are a few morning rituals that will start your day on the right foot for years to come. Lorem ipsum dolor sit amet, consectetur adipiscing elit, sed do eiusmod tempor incididunt ut labore et dolore magna aliqua. Ut enim ad minim veniam, quis nostrud exercitation ullamco laboris nisi ut aliquip ex ea commodo consequat.</p>
      <p>Duis aute irure dolor in reprehenderit in voluptate velit esse cillum dolore eu fugiat nulla pariatur. Excepteur sint occaecat cupidatat non proident, sunt in culpa qui officia deserunt mollit anim id est laborum.</p>
    </div>

    <div class="offer-band">TRY 3 ACUPUNCTURE SESSIONS FROM US FOR ONLY</div>
    <div class="price price-weekday">weekdays <span class="price-amount"><sup>$</sup>150</span></div>
    <div class="price price-weekend">weekends <span class="price-amount"><sup>$</sup>175</span></div>

    <div class="contact contact-web">www.thornburyacupuncture.com</div>
    <div class="contact contact-tel">Tel No.: (02) 555 018 2746</div>
  </main>
</body>
</html>
```